Trvmlegal.com needs a wedsite. Law Office of Darnell P. Whitby

Darnell P. Whitby is a criminal law firm that is 5 years old. We have already had all the content written and now just need the website designed. We also just finished our logo design using Pixel Harbor and would like it used in the design of the website.

Industry/Entity Type

Law Firm

Number of Pages Required

5+ page

Requirements
Must have
• I was our new logo to be on the website also. I want Dallas sites as the stock pictures for the website. For example the Grey Stone Tribunal. I also need to be able to add YouTube videos. It has to adjust to be seen on computers and also cell phones. I need to be able to have a information sheet for clients to fill out and submit back to me.

```html
<!DOCTYPE html>
<html lang="en">
<head>
<meta charset="utf-8">
<title>Law Office of Darnell P. Whitby</title>
<link rel="stylesheet" href="https://fonts.googleapis.com/css2?family=Gelasio:wght@400;500&family=Roboto:wght@400;500&display=swap">
<style>
:root{
  --navy:#0b2a78;
  --navy-btn:#0a2a80;
  --ink:#333;
  --muted:#666;
  --line:#e2e2e2;
  --beige:#f0efe1;
  --dark-panel:#2f2f2f;
  --white:#fff;
  --icon:#555;
}
*{margin:0;padding:0;box-sizing:border-box}
html,body{width:755px;height:1200px;overflow:hidden;background:var(--white)}
body{position:relative;font-family:"Roboto",sans-serif;color:var(--ink)}
.abs{position:absolute}
.serif{font-family:"Gelasio",serif}

/* header */
.brand{left:50px;top:8px;width:76px;height:76px;border-radius:50%;background:var(--navy);display:flex;align-items:center;justify-content:center;color:var(--white);font-family:"Gelasio",serif;font-size:20px}
.brand-name{left:0;top:86px;width:0;overflow:hidden}
.nav{left:196px;top:33px;display:flex;gap:0}
.nav a{font-family:"Gelasio",serif;font-size:10px;line-height:10px;color:var(--ink);text-decoration:none;text-align:center;display:block}
.nav a.active{color:var(--navy)}

/* hero */
.hero-photo{left:0;top:92px;width:444px;height:328px;background:linear-gradient(160deg,#8a8a88 0%,#6f706e 45%,#4a4b4a 100%)}
.hero-title{left:50px;top:190px;color:var(--white);font-family:"Gelasio",serif;font-size:27px;letter-spacing:2px;line-height:33px}
.hero-sub{left:50px;top:272px;color:var(--white);font-size:10px;line-height:14.5px}
.dots{left:352px;top:386px;display:flex;gap:9px}
.dots span{width:10px;height:10px;border-radius:50%;background:var(--white)}
.dots span.off{background:transparent;border:1px solid var(--white)}
.consult{left:444px;top:92px;width:311px;height:328px;background:linear-gradient(180deg,#3a3a3a,#262626)}
.consult h2{position:absolute;left:27px;top:25px;font-family:"Gelasio",serif;font-weight:400;font-size:20px;color:var(--white)}
.field{position:absolute;left:25px;width:210px;height:33px;background:var(--white);border-radius:2px;font-size:9px;color:#888;padding:9px 8px}
.submit{position:absolute;left:25px;top:270px;width:210px;height:26px;background:var(--navy-btn);color:var(--white);font-size:11.5px;text-align:center;line-height:26px}

/* news */
.section-title{left:0;width:755px;text-align:center;font-family:"Gelasio",serif;font-weight:400}
.news-title{top:455px;font-size:29px;color:var(--ink)}
.card{top:500px;width:155px;height:96px;border:1px solid var(--line);padding:2px;background:var(--white)}
.card .thumb{width:100%;height:100%;position:relative}
.card svg{position:absolute;left:50%;top:50%;transform:translate(-50%,-50%)}
.caption{top:609px;width:155px;text-align:center;font-size:12px;color:var(--muted)}
.caption.active{color:var(--navy)}

/* about */
.about{left:0;top:662px;width:755px;height:151px;background:var(--beige)}
.about h2{position:absolute;top:35px;width:755px;text-align:center;font-family:"Gelasio",serif;font-weight:400;font-size:28px;color:#7a7a72}
.about p{position:absolute;left:100px;top:86px;width:555px;text-align:center;font-size:9.2px;line-height:14.5px;color:var(--muted)}

/* services */
.service{top:845px;width:160px;text-align:center}
.service svg{display:block;margin:0 auto}
.service .label{display:inline-block;margin-top:14px;font-size:13px;color:var(--muted);padding-bottom:1px}
.service .label.active{color:var(--navy);border-bottom:1px solid var(--navy)}

/* contact band */
.contact{left:0;top:977px;width:755px;height:196px;background:var(--navy)}
.contact-info{position:absolute;right:467px;top:65px;text-align:right;color:var(--white);font-size:13.5px;line-height:23px}
.portrait{position:absolute;left:311px;top:32px;width:133px;height:132px;border:2px solid var(--white);background:linear-gradient(180deg,#6a5a4a,#2a2420)}
.bio{position:absolute;left:463px;top:61px;width:185px;font-size:8.6px;font-weight:500;line-height:14.5px;color:#dfe4f2}

/* footer */
.social{left:58px;top:1181px;display:flex;gap:10px}
.social span{width:8px;height:8px;border-radius:50%;background:#b5b5b5}
.social span:first-child{background:var(--navy)}
.copy{right:50px;top:1180px;font-size:9.5px;color:var(--muted)}
</style>
</head>
<body>

<header>
  <div class="abs brand" aria-label="Law Office of Darnell P. Whitby">DPW</div>
  <nav class="abs nav">
    <a class="active" href="#" style="width:64px">How We<br>Can Help</a>
    <a href="#" style="width:76px">Sexual<br>Offenses</a>
    <a href="#" style="width:88px">Early Probation<br>Release</a>
    <a href="#" style="width:74px">Probation<br>Violations</a>
    <a href="#" style="width:92px">Other Violent<br>Offenses</a>
    <a href="#" style="width:54px">DWI/<br>DUI</a>
    <a href="#" style="width:76px">Drug<br>Offenses</a>
  </nav>
</header>

<section>
  <div class="abs hero-photo" role="img" aria-label="Grey textured stone courthouse wall"></div>
  <h1 class="abs hero-title">INITIAL<br>CONSULTATION!</h1>
  <p class="abs hero-sub">AFFORDABLE<br>PAYMENT PLANS</p>
  <div class="abs dots"><span class="off"></span><span></span><span></span></div>

  <form class="abs consult">
    <h2>Consultation!</h2>
    <div class="field" style="top:67px">Name</div>
    <div class="field" style="top:106px">E Mail</div>
    <div class="field" style="top:145px">Phone</div>
    <div class="field" style="top:185px;height:65px">Message</div>
    <div class="submit">SUBMIT YOUR MESSAGE</div>
  </form>
</section>

<section>
  <h2 class="abs section-title news-title">LATEST NEWS</h2>

  <div class="abs card" style="left:50px"><div class="thumb" role="img" aria-label="Lawyer meeting a client at a desk" style="background:linear-gradient(135deg,#6b5040,#3a3634 50%,#cfcac4)">
    <svg width="20" height="20" viewBox="0 0 20 20"><circle cx="10" cy="10" r="8.5" fill="none" stroke="#fff" stroke-width="2"/><path d="M8 6l6 4-6 4z" fill="#fff"/></svg></div></div>
  <div class="abs card" style="left:216px"><div class="thumb" role="img" aria-label="Gavel and scales of justice in warm light" style="background:linear-gradient(135deg,#c0602a,#6a2a10 60%,#d89a4a)">
    <svg width="20" height="20" viewBox="0 0 20 20"><circle cx="10" cy="10" r="8.5" fill="none" stroke="#fff" stroke-width="2"/><path d="M8 6l6 4-6 4z" fill="#fff"/></svg></div></div>
  <div class="abs card" style="left:383px"><div class="thumb" role="img" aria-label="Handshake across an office desk" style="background:linear-gradient(135deg,#d8d8d8,#2a2a2e 50%,#7a7e88)">
    <svg width="20" height="20" viewBox="0 0 20 20"><circle cx="10" cy="10" r="8.5" fill="none" stroke="#fff" stroke-width="2"/><path d="M8 6l6 4-6 4z" fill="#fff"/></svg></div></div>
  <div class="abs card" style="left:549px"><div class="thumb" role="img" aria-label="Handcuffed hands resting on a table" style="background:linear-gradient(180deg,#6a3a2a,#a86a4a 55%,#5a2818)">
    <svg width="20" height="20" viewBox="0 0 20 20"><circle cx="10" cy="10" r="8.5" fill="none" stroke="#fff" stroke-width="2"/><path d="M8 6l6 4-6 4z" fill="#fff"/></svg></div></div>

  <p class="abs caption active" style="left:50px">Probatio Violations</p>
  <p class="abs caption" style="left:216px">Homicide Offenses</p>
  <p class="abs caption" style="left:383px">Expungements</p>
  <p class="abs caption" style="left:549px">Murder Offenses</p>
</section>

<section class="abs about">
  <h2>THE DPW LAW OFFICE</h2>
  <p>Lorem Ipsum is simply dummy text of the printing and typesetting industry. Lorem Ipsum has been the industry's standard dummy text ever since the 1500s, when an unknown printer took a galley of type and scrambled it to make.</p>
</section>

<section>
  <div class="abs service" style="left:73px">
    <svg width="60" height="54" viewBox="0 0 60 54" fill="none" stroke="var(--navy)" stroke-width="4" stroke-linecap="round">
      <path d="M10 50L46 8M50 50L14 8"/><path d="M6 8h14M40 8h14" stroke-width="3"/><path d="M18 36l8 6M42 36l-8 6" stroke-width="3"/>
    </svg>
    <span class="label active">Personal Injury</span>
  </div>
  <div class="abs service" style="left:297px">
    <svg width="70" height="54" viewBox="0 0 70 54" fill="none" stroke="var(--icon)" stroke-width="3">
      <circle cx="17" cy="28" r="13"/><circle cx="52" cy="36" r="13"/>
      <path d="M26 16c3-5 8-7 12-5s6 4 10 6" stroke-width="2"/><circle cx="40" cy="8" r="3" stroke-width="2"/><circle cx="49" cy="10" r="3" stroke-width="2"/>
    </svg>
    <span class="label">Criminal</span>
  </div>
  <div class="abs service" style="left:521px">
    <svg width="70" height="54" viewBox="0 0 70 54" fill="var(--icon)">
      <path d="M4 30l6-12h18l6 12v14h-6v-4H10v4H4z"/><path d="M38 28l10-12 16 6 2 14-4 8-6-2 1-4-14-5-1 4-6-2z"/>
      <rect x="8" y="32" width="5" height="3" fill="#fff"/><rect x="25" y="32" width="5" height="3" fill="#fff"/>
      <path d="M34 4v8M28 8l4 6M40 8l-4 6" stroke="var(--icon)" stroke-width="2"/>
    </svg>
    <span class="label">Auto Accident</span>
  </div>
</section>

<section class="abs contact">
  <div class="contact-info">Darnell P. Whitby,Lawyer<br>5550142876<br>@darnellwhitbylaw.com</div>
  <div class="portrait" role="img" aria-label="Portrait of the lawyer in court robes"></div>
  <p class="bio">Lorem Ipsum is simply dummy text of the printing and typesetting industry. Lorem Ipsum has been the industry's standard dummy text ever since the 1500s, when an unknown printer took a galley of type and scrambled it to make</p>
</section>

<footer>
  <div class="abs social" aria-label="Social links"><span></span><span></span><span></span><span></span><span></span></div>
  <p class="abs copy">© Law Office of DPW&nbsp; 2015. All Rights Reserved.</p>
</footer>

</body>
</html>
```